Website for Reiki and Wellness Courses

I teach online courses in Reiki and wellness/self-development and am needing a new website.

The focus of the website will be to provide descriptions of the courses as well as include a blog and pages where students in my courses will visit for additional information.

Note: courses are NOT hosted on this site.
The focus of this website will be to encourage viewers to enroll in courses as well as opt in to the email list.

I will upload copy soon. My old website is: http://calmstreamlessons.example. Please do not use existing logo.

Target Market(s)

Alternative health, wellness, spirituality, personal development. Males and females of all ages seeking to improve their health and life.

Industry/Entity Type

Health And Wellness

Logo Text

No text (please do not use existing logo)

Coding

Coded - Design and coding required

Number of Pages Required

5+ page

Requirements
Must have
• 1. Home page
• 2. About page
• 3. Courses page that outlines courses (there are currently 6 courses with 1 coming soon)
• 4. Individual course page (maybe a template that I can adjust color and pictures for with each course)
• 5. Blog
• 6. Student Area that outlines all Student Areas
• 7. Individual Student Area page (maybe a template that I can adjust color and pictures for with each course)
• 8. Shop page (note: items will not currently be purchased through website - it will be a link to brightmart for a book).
• 9. Student thank-you page (maybe a template that I can adjust color and pictures for with each course) this is the page students are directed to at end of course with vouchers for other courses.
• Opt-in for the home page, course pages, blog and thank-you pages
Nice to have
• I would like the design to be calm, clean and soothing. Ideally visitors feel relaxed when viewing the site and are encouraged to explore the courses, subscribe to the email list and purchase a product.
• ~ Testimonials page
• ~ Contact page
• I tend to gravitate towards blues, greys and purples as well as monochromatic color schemes.
Should not have
• Contact form on home page
• phone number on home page
• location/physical address
• dates for blog posts

```html
<!DOCTYPE html>
<html lang="en">
<head>
<meta charset="utf-8">
<title>Calmstream Lessons</title>
<link href="https://fonts.googleapis.com/css2?family=Raleway:wght@300;400;500;600;700&family=Montserrat:wght@500;600&family=Jost:ital,wght@0,400;0,500;1,400&display=swap" rel="stylesheet">
<style>
:root{
  --slate:#7a7b99;
  --slate-dark:#626381;
  --mauve:#b57aae;
  --plum:#5c3a5e;
  --ink:#222226;
  --text:#555;
  --light:#ececee;
  --footer-dark:#2a2a2c;
  --white:#fff;
}
*{box-sizing:border-box;margin:0;padding:0}
html,body{width:1200px;height:2985px;overflow:hidden}
body{font-family:"Jost",sans-serif;color:var(--text);background:var(--white);position:relative}
.abs{position:absolute}

/* top bar */
.topbar{position:absolute;top:0;left:0;width:1200px;height:40px;background:var(--slate)}
.topbar .icons{position:absolute;right:160px;top:7px;display:flex;gap:6px}
.topbar .icons span{width:24px;height:24px;border-radius:50%;background:#9a9bb4;display:block}

/* header */
.header{position:absolute;top:40px;left:0;width:1200px;height:70px;background:var(--white)}
.brand{position:absolute;left:163px;top:14px;display:flex;align-items:center;gap:10px}
.brand .mark{width:34px;height:34px;border-radius:50%;background:var(--slate)}
.brand .name{font-family:"Raleway",sans-serif;font-weight:600;font-size:21px;color:var(--slate-dark);letter-spacing:1px;line-height:1}
.nav{position:absolute;left:412px;top:-4px;display:flex;height:74px}
.nav a{font-family:"Montserrat",sans-serif;font-weight:600;font-size:11px;color:var(--ink);text-decoration:none;text-transform:uppercase;padding:0 19px;line-height:74px}
.nav a.active{background:var(--slate);color:var(--white);padding:0 20px}

/* hero */
.hero{position:absolute;top:110px;left:0;width:1200px;height:440px;overflow:hidden;
  background:
    radial-gradient(ellipse 190px 130px at 700px 340px,rgba(74,48,36,.85),rgba(74,48,36,0) 70%),
    radial-gradient(ellipse 150px 95px at 830px 250px,rgba(214,170,146,.95),rgba(214,170,146,0) 72%),
    radial-gradient(ellipse 120px 60px at 980px 95px,rgba(222,196,180,.8),rgba(222,196,180,0) 72%),
    radial-gradient(ellipse 230px 110px at 1080px 230px,rgba(176,168,176,.7),rgba(176,168,176,0) 72%),
    radial-gradient(ellipse 340px 90px at 880px 420px,rgba(255,255,255,.95),rgba(255,255,255,0) 72%),
    radial-gradient(ellipse 140px 220px at 1000px 0px,rgba(250,250,250,.9),rgba(250,250,250,0) 72%),
    linear-gradient(90deg,#f3f3f5 0%,#efeff1 45%,#e6e3e5 68%,#dedadc 100%)}
.hero-title{position:absolute;left:163px;top:150px;font-family:"Raleway",sans-serif;font-weight:500;font-size:34px;line-height:37px;color:var(--mauve)}
.hero-sub{position:absolute;left:165px;top:234px;font-family:"Raleway",sans-serif;font-weight:600;font-size:14px;color:var(--ink)}
.btn{display:inline-block;background:var(--slate);color:var(--white);font-family:"Raleway",sans-serif;font-weight:600;font-size:12px;text-align:center}
.hero .btn{position:absolute;left:163px;top:264px;width:104px;height:28px;line-height:28px}
.hero-arrow{position:absolute;left:6px;top:200px;width:30px;height:28px;background:#333}
.float-share{position:absolute;right:0;top:125px;width:40px;height:168px;background:var(--white);display:flex;flex-direction:column;align-items:center;justify-content:space-around;padding:4px 0}
.float-share span{width:24px;height:24px;border-radius:50%;background:var(--slate)}

/* section headings */
.sec-title{position:absolute;left:0;width:1200px;text-align:center;font-family:"Raleway",sans-serif;font-weight:600;font-size:28px;color:var(--ink)}
.sec-title em{font-style:normal;font-weight:500;color:var(--mauve)}
.divider{position:absolute;left:520px;width:160px;height:12px}

/* about */
.about{position:absolute;top:550px;left:0;width:1200px;height:435px;background:var(--white)}
.tabs{position:absolute;left:163px;top:135px;width:192px;height:244px;border-right:2px solid #aaa}
.tabs li{list-style:none;text-align:right;padding-right:20px;font-family:"Raleway",sans-serif;font-weight:500;font-size:13px;color:var(--ink);height:41px;line-height:41px;text-transform:uppercase}
.tabs li.active{color:var(--mauve);border:1px solid #aaa;border-right:none;height:40px;width:194px;background:var(--white)}
.about-text{position:absolute;left:378px;top:130px;width:392px;font-size:11.5px;line-height:21px;color:var(--text)}
.about-text p{margin-bottom:9px}
.about-photo{position:absolute;left:792px;top:133px;width:247px;height:247px;border:1px solid #bbb;padding:4px;background:var(--white)}
.about-photo div{width:100%;height:100%;
  background:
    radial-gradient(ellipse 60px 80px at 50% 48%,rgba(226,190,170,.95),rgba(226,190,170,0) 75%),
    radial-gradient(ellipse 110px 60px at 50% 18%,rgba(90,64,50,.8),rgba(90,64,50,0) 75%),
    linear-gradient(90deg,#e9e6e6,#f4f2f2 50%,#e6e2e2)}
.about-photo:after{content:"";position:absolute;right:-1px;bottom:-6px;width:100px;height:6px;background:var(--mauve)}

/* feature band */
.feature{position:absolute;top:985px;left:0;width:1200px;height:480px;overflow:hidden;
  background:radial-gradient(ellipse at 50% 45%,#c8b0c9 0%,#9a7399 35%,#744e74 75%,#5f3f61 100%)}
.feature .beam{position:absolute;left:440px;top:0;width:320px;height:480px;
  background:radial-gradient(ellipse 160px 300px at 50% 30%,rgba(255,255,255,.55),rgba(255,255,255,0) 75%)}
.feature .lotus{position:absolute;left:380px;top:300px;width:460px;height:180px;
  background:
    radial-gradient(ellipse 230px 120px at 50% 100%,rgba(255,255,255,.95),rgba(255,255,255,.55) 45%,rgba(255,255,255,0) 80%),
    radial-gradient(ellipse 90px 120px at 20% 70%,rgba(240,232,242,.6),rgba(240,232,242,0) 75%),
    radial-gradient(ellipse 90px 120px at 80% 70%,rgba(240,232,242,.6),rgba(240,232,242,0) 75%)}
.feat-block{position:absolute;color:var(--white);font-family:"Raleway",sans-serif}
.feat-block h3{font-weight:600;font-size:18px;margin-bottom:10px}
.feat-block p{font-weight:600;font-size:11px;line-height:16px}
.feat-left{left:160px;top:168px;width:225px;text-align:right}
.feat-right{left:865px;top:168px;width:220px}
.feat-cta{position:absolute;left:0;top:371px;width:1200px;text-align:center;font-family:"Raleway",sans-serif}
.feat-cta h3{font-weight:700;font-size:19px;color:var(--plum)}
.feat-cta p{font-weight:600;font-size:11px;color:var(--plum);margin-top:4px}
.feature svg{position:absolute;left:0;top:0}

/* newsletter */
.inspire{position:absolute;top:1465px;left:0;width:1200px;height:282px;background:var(--light)}
.inspire .lead{position:absolute;left:220px;top:127px;width:760px;text-align:center;font-size:11.5px;line-height:18px;color:#444}
.field{position:absolute;top:187px;height:30px;background:var(--white);border:1px solid #ddd;font-size:10px;color:#888;padding-left:8px;line-height:28px}
.inspire .btn{position:absolute;left:802px;top:187px;width:167px;height:30px;line-height:30px}

/* blog */
.blog{position:absolute;top:1747px;left:0;width:1200px;height:521px;background:var(--white)}
.card{position:absolute;top:135px;width:274px}
.card .thumb{height:132px}
.card h4{font-family:"Raleway",sans-serif;font-weight:500;font-size:13px;color:var(--mauve);margin-top:14px}
.card p{font-size:10.5px;line-height:16px;color:#555;margin-top:5px}
.card a{display:block;margin-top:12px;font-size:10.5px;font-weight:500;color:var(--ink);text-decoration:underline}
.blog .btn{position:absolute;left:531px;top:426px;width:138px;height:30px;line-height:30px}

/* testimonials */
.love{position:absolute;top:2268px;left:0;width:1200px;height:399px;
  background:linear-gradient(90deg,#eadcd7 0%,#f3eeee 30%,#f7f6f6 55%,#f1ebea 75%,#e4d6d2 100%)}
.quote{position:absolute;left:232px;top:118px;width:736px;text-align:center;font-style:italic;font-size:13.5px;line-height:21px;color:#333}
.quote-line{position:absolute;left:230px;top:208px;width:740px;height:1px;background:#bbb}
.avatar{position:absolute;border-radius:50%;border:3px solid var(--white);box-shadow:0 2px 4px rgba(0,0,0,.25)}
.love .who{position:absolute;left:0;top:336px;width:1200px;text-align:center;font-family:"Raleway",sans-serif;font-weight:600;font-size:12px;color:var(--ink)}

/* footer */
.footer{position:absolute;top:2667px;left:0;width:1200px;height:278px;background:var(--slate)}
.footer svg.split{position:absolute;left:0;top:0}
.footer h5{position:absolute;font-family:"Raleway",sans-serif;font-weight:700;font-size:17px;color:var(--white);letter-spacing:.5px}
.quick{position:absolute;left:163px;top:88px;list-style:none}
.quick li{font-size:11.5px;color:#ddd;height:24px}
.footer .note{position:absolute;left:460px;top:82px;font-size:11px;line-height:17px;color:#c7c8da;width:170px}
.footer .mail{position:absolute;left:458px;top:160px;width:200px;height:26px;background:#3a3a40;font-size:9.5px;color:#ccc;padding-left:8px;line-height:26px}
.footer .send{position:absolute;left:658px;top:160px;width:88px;height:26px;background:#eee;font-size:11px;font-weight:500;color:var(--ink);padding-left:5px;line-height:26px}
.footer .follow{position:absolute;left:455px;top:233px;font-size:15px;color:var(--white)}
.footer .follow-icons{position:absolute;left:541px;top:231px;display:flex;gap:7px}
.footer .follow-icons span{width:22px;height:22px;border-radius:50%;background:#9c9db6}
.footer .vline{position:absolute;left:792px;top:50px;width:1px;height:200px;background:#9495b0}
.footer .fbrand{position:absolute;left:830px;top:205px;width:230px;text-align:center;font-family:"Raleway",sans-serif;font-weight:600;font-size:19px;color:#b7b8cc;letter-spacing:1px}
.footer .fmark{position:absolute;left:910px;top:115px;width:70px;height:70px;border-radius:50%;background:#8d8ea9}
.copy{position:absolute;top:2945px;left:0;width:1200px;height:40px;background:#111;color:#bbb;text-align:center;font-size:10.5px;line-height:40px}
.copy b{color:var(--white);font-weight:500}
</style>
</head>
<body>

<div class="topbar"><div class="icons"><span></span><span></span><span></span><span></span><span></span><span></span></div></div>

<header class="header">
  <div class="brand"><span class="mark"></span><span class="name">Calmstream<br>Lessons</span></div>
  <nav class="nav">
    <a class="active" href="#">Home</a><a href="#">About Us</a><a href="#">Courses</a><a href="#">Student Areas</a><a href="#">Blog</a><a href="#">Testimonials</a><a href="#">Contact</a>
  </nav>
</header>

<section class="hero" role="img" aria-label="Photo of a woman lying relaxed on a white towel while a practitioner holds hands above her in a Reiki session">
  <div class="hero-arrow"><svg width="30" height="28"><path d="M18 8 L12 14 L18 20" stroke="#fff" stroke-width="3" fill="none"/></svg></div>
  <h1 class="hero-title">Time For Change In<br>Your Life</h1>
  <p class="hero-sub">What Would It Be Like To Live The Life You Were Meant To Live?</p>
  <span class="btn">Know More</span>
  <div class="float-share"><span></span><span></span><span></span><span></span><span></span></div>
</section>

<section class="about">
  <h2 class="sec-title" style="top:50px">About <em>Calmstream Lessons</em></h2>
  <svg class="divider" style="top:96px" viewBox="0 0 160 12"><line x1="0" y1="6" x2="160" y2="6" stroke="#333"/><circle cx="80" cy="6" r="3.5" fill="#fff" stroke="#333"/></svg>
  <ul class="tabs">
    <li class="active">What We Do</li><li>Story &amp; History</li><li>Values &amp; Philosophy</li><li>Mission &amp; Services</li><li>Our Skills</li><li>Honors &amp; Awards</li>
  </ul>
  <div class="about-text">
    <p>Lorem ipsum dolor sit amet, consectetuer adipiscing elit, sed diam nonummy nibh hfd dautieuismod tincidunt ut laoreet dolore magna aliquam erat volutpat. Ut wisi enim ad minim veniam quis nostrud exerci tation ullamcorper suscipit.</p>
    <p>- Duis autem vel eum iriure dolor in hendrerit in vulputate velit ese molestie.Ut wisi enim ad minim veniam quis nostrud exerci.</p>
    <p>- Sed diam nonummy nibh hfd dautieuismod tincidunt ut laoreet.- dautieuismod tincidunt ut laoreet.</p>
    <p>- Sed diam nonummy nibh hfd dautieuismod tincidunt ut laoreet.</p>
    <p>- Duis autem vel eum iriure dolor in hendrerit in vulputate velit esse.</p>
  </div>
  <div class="about-photo"><div role="img" aria-label="Photo of a woman with closed eyes receiving a head treatment"></div></div>
</section>

<section class="feature">
  <div class="beam" role="img" aria-label="Soft sparkling light rising from the centre"></div>
  <div class="lotus" role="img" aria-label="Glowing white lotus flower illustration"></div>
  <svg width="1200" height="480" viewBox="0 0 1200 480">
    <defs>
      <radialGradient id="disc" cx="50%" cy="45%" r="55%">
        <stop offset="0" stop-color="#ffffff"/>
        <stop offset="1" stop-color="#efe4ee"/>
      </radialGradient>
      <radialGradient id="discCore" cx="50%" cy="50%" r="55%">
        <stop offset="0" stop-color="#c9a8c6"/>
        <stop offset="1" stop-color="#9c7199"/>
      </radialGradient>
      <radialGradient id="topGlow" cx="50%" cy="50%" r="50%">
        <stop offset="0" stop-color="#ffffff" stop-opacity=".95"/>
        <stop offset="1" stop-color="#ffffff" stop-opacity="0"/>
      </radialGradient>
    </defs>
    <g fill="none" stroke="#fff" stroke-width="1.5" stroke-dasharray="3 4">
      <path d="M470 165 Q505 125 570 118"/>
      <path d="M770 165 Q735 125 670 118"/>
      <line x1="622" y1="150" x2="622" y2="232"/>
    </g>
    <g fill="#fff">
      <path d="M572 118 l-10 -5 v10z"/>
      <path d="M668 118 l10 -5 v10z"/>
      <path d="M622 146 l-5 10 h10z"/>
    </g>
    <circle cx="622" cy="105" r="46" fill="url(#topGlow)" role="img" aria-label="Emblem of a seated figure in meditation"/>
    <g role="img" aria-label="Icon of an open hand">
      <circle cx="450" cy="224" r="52" fill="url(#disc)"/>
      <circle cx="450" cy="224" r="42" fill="none" stroke="#a985a6" stroke-width="2"/>
    </g>
    <g role="img" aria-label="Icon of a person meditating">
      <circle cx="795" cy="224" r="52" fill="url(#disc)"/>
      <circle cx="795" cy="224" r="42" fill="none" stroke="#a985a6" stroke-width="2"/>
    </g>
    <g role="img" aria-label="Mandala emblem">
      <circle cx="622" cy="300" r="56" fill="#fff"/>
      <circle cx="622" cy="300" r="47" fill="url(#discCore)"/>
      <circle cx="622" cy="300" r="30" fill="none" stroke="#fff" stroke-opacity=".7"/>
      <circle cx="622" cy="300" r="14" fill="none" stroke="#fff" stroke-opacity=".7"/>
    </g>
  </svg>
  <div class="feat-block feat-left"><h3>How Reiki Works</h3><p>Reiki Has Been Used For Centuries To Help Individuals With Physical &amp; Emotional Imbalances As Well As Those Seeking Clarity &amp; Enlightenment.</p></div>
  <div class="feat-block feat-right"><h3>Resources</h3><p>Information And Tools To Help You Create A Life You Love.</p></div>
  <div class="feat-cta"><h3>Traditional Usui Reiki Master Certification</h3><p>Learn how to use Reiki to help yourself and others.</p></div>
</section>

<section class="inspire">
  <h2 class="sec-title" style="top:52px">Stay <em>Inspired</em></h2>
  <svg class="divider" style="top:97px" viewBox="0 0 160 12"><line x1="0" y1="6" x2="160" y2="6" stroke="#333"/><circle cx="80" cy="6" r="3.5" fill="#ececee" stroke="#333"/></svg>
  <p class="lead">Receive Information And Articles Each Month To Keep You Feeling Inspired. As A Thank-you, You Will Also Receive Access To Soothing Music You Can Download For Use In Your Reiki Sessions And Meditation.</p>
  <div class="field" style="left:231px;width:181px">First Name</div>
  <div class="field" style="left:422px;width:179px">Last Name</div>
  <div class="field" style="left:611px;width:179px">Email Add...</div>
  <span class="btn">Yes-Count Me In</span>
</section>

<section class="blog">
  <h2 class="sec-title" style="top:56px">Latest <em>Blog</em></h2>
  <svg class="divider" style="top:101px" viewBox="0 0 160 12"><line x1="0" y1="6" x2="160" y2="6" stroke="#333"/><circle cx="80" cy="6" r="3.5" fill="#fff" stroke="#333"/></svg>
  <article class="card" style="left:163px">
    <div class="thumb" role="img" aria-label="Photo of a man receiving a Reiki treatment" style="background:linear-gradient(110deg,#d9d0cb,#8e817c 55%,#222)"></div>
    <h4>Aisi enim aminim moramet...</h4>
    <p>Lorem ipsum dolor sit aconsectetuer adip iscing elit, sediam nonummy nibh euismod tincidunt ut laoreet dolore magna aliquam erat volut min nostrud .</p>
    <a href="#">Read More »</a>
  </article>
  <article class="card" style="left:462px">
    <div class="thumb" role="img" aria-label="Photo of a smooth stone on raked sand" style="background:radial-gradient(circle at 48% 55%,#7d7670 0,#9a928b 18%,#d8d1c8 30%,#c9c0b6 100%)"></div>
    <h4>Aisi enim aminim moramet...</h4>
    <p>Lorem ipsum dolor sit aconsectetuer adip iscing elit, sediam nonummy nibh euismod tincidunt ut laoreet dolore magna aliquam erat volut min nostrud .</p>
    <a href="#">Read More »</a>
  </article>
  <article class="card" style="left:764px">
    <div class="thumb" role="img" aria-label="Photo of stacked pebbles on a beach by the sea" style="background:linear-gradient(180deg,#3fa3c0 0%,#8fc7d6 25%,#b9b1a6 45%,#6d655d 100%)"></div>
    <h4>Aisi enim aminim moramet...</h4>
    <p>Lorem ipsum dolor sit aconsectetuer adip iscing elit, sediam nonummy nibh euismod tincidunt ut laoreet dolore magna aliquam erat volut min nostrud .</p>
    <a href="#">Read More »</a>
  </article>
  <span class="btn">View More</span>
</section>

<section class="love" role="img" aria-label="Faded photo of a woman receiving a Reiki head treatment">
  <h2 class="sec-title" style="top:48px">People <em>Love Us!</em></h2>
  <svg class="divider" style="top:92px" viewBox="0 0 160 12"><line x1="0" y1="6" x2="160" y2="6" stroke="#333"/><circle cx="80" cy="6" r="3.5" fill="#f5f3f3" stroke="#333"/></svg>
  <p class="quote">“ Lorem ipsum dolor sit amet, consectetuer adipiscing elit, sed diam nonumy nibh euismod tincidunt ut laoreet dolore magna aliquam erat volutpat. Lorem ipsum dolor sit amet, consectetuer adipiscing elit, seiam nonummy nibh euismod tincidunt ut laoreet dolore magna aliquam volutpat. ”</p>
  <div class="quote-line"></div>
  <svg class="abs" style="left:592px;top:208px" width="16" height="8"><path d="M0 0 L8 8 L16 0z" fill="#888"/></svg>
  <div class="avatar" role="img" aria-label="Portrait of a client" style="left:473px;top:245px;width:64px;height:64px;background:#b9a496"></div>
  <div class="avatar" role="img" aria-label="Portrait of Mira Calloway" style="left:564px;top:240px;width:74px;height:74px;background:#a78e82;border-color:#c9a7c4"></div>
  <div class="avatar" role="img" aria-label="Portrait of a client" style="left:661px;top:245px;width:64px;height:64px;background:#c7ab9c"></div>
  <p class="who">Miss. Mira Calloway</p>
</section>

<footer class="footer">
  <svg class="split" width="420" height="278"><path d="M0 0 H408 L380 278 H0z" fill="#2a2a2c"/></svg>
  <h5 style="left:163px;top:48px">QUICK LINKS</h5>
  <ul class="quick"><li>Home</li><li>About Us</li><li>Courses</li><li>Student Areas</li><li>Blog</li><li>Testimonials</li><li>Contact</li></ul>
  <h5 style="left:458px;top:48px">NEWSLETTER SIGNUP</h5>
  <p class="note">Get the latest updates by entering your email address</p>
  <svg class="abs" style="left:695px;top:100px" width="56" height="40"><path d="M2 18 L54 2 L30 38 L24 22z" fill="none" stroke="#3a3a40" stroke-width="2"/></svg>
  <div class="mail">Enter your email here</div>
  <div class="send">Subscribe</div>
  <span class="follow">Follow Us:</span>
  <div class="follow-icons"><span></span><span></span><span></span><span></span><span></span><span></span></div>
  <div class="vline"></div>
  <div class="fmark"></div>
  <div class="fbrand">Calmstream Lessons</div>
</footer>
<div class="copy">Copyright © 2016 <b>Calmstream Lessons</b>. All Right Reserved</div>

</body>
</html>
```